Tidewell Pest Solutions *

I work as a pest control technician with other company. Now I want to start my own business.

So I want a new logo and business card design (both side of the card).

Colour combination I like Green/Red/white.

On card may have some sort of insect/ but not sure.

Target Market(s)

Anyone in Sydney. There is no specific target.

Industry/Entity Type

Business

Logo Text

Tidewell Pest Solutions

```html
<!DOCTYPE html>
<html lang="en">
<head>
<meta charset="utf-8">
<title>Tidewell Pest Solutions – Business Card</title>
<link rel="stylesheet" href="https://fonts.googleapis.com/css2?family=Arimo:wght@400;700&display=swap">
<style>
  :root {
    --backdrop: #555555;
    --card-white: #ffffff;
    --charcoal: #3a3536;
    --brand-red: #d10000;
    --ink: #1e1e1e;
    --rule: #9a97a8;
  }
  html, body {
    margin: 0;
    padding: 0;
    width: 1200px;
    height: 900px;
    overflow: hidden;
    background: var(--backdrop);
    font-family: "Arimo", Arial, sans-serif;
  }
  .canvas {
    position: relative;
    width: 1200px;
    height: 900px;
  }
  .card {
    position: absolute;
    top: 170px;
    width: 347px;
    height: 561px;
    overflow: hidden;
  }
  .card--front { left: 259px; background: var(--card-white); }
  .card--back { left: 631px; background: var(--charcoal); }

  /* Front: brand name */
  .brand {
    position: absolute;
    left: 40px;
    top: 130px;
    display: flex;
    align-items: center;
    gap: 14px;
  }
  .brand__dot {
    width: 68px;
    height: 68px;
    border-radius: 50%;
    background: var(--charcoal);
    flex: none;
  }
  .brand__name {
    margin: 0;
    width: 180px;
    font-family: "Arimo", Arial, sans-serif;
    font-weight: 700;
    font-size: 24px;
    line-height: 28px;
    color: var(--brand-red);
  }

  /* Front: contact block */
  .contact {
    position: absolute;
    left: 0;
    right: 0;
    top: 325px;
    text-align: center;
    color: var(--ink);
  }
  .contact__name {
    margin: 0;
    font-size: 21px;
    font-weight: 700;
    color: var(--brand-red);
    line-height: 26px;
  }
  .contact__role {
    margin: 0;
    font-size: 15px;
    line-height: 20px;
  }
  .contact__icons {
    display: block;
    margin: 9px auto 4px;
  }
  .contact__line {
    margin: 0;
    font-size: 15px;
    line-height: 21px;
  }
  .contact__rule {
    width: 156px;
    height: 1px;
    background: var(--rule);
    margin: 10px auto 12px;
  }
  .contact__address {
    margin: 0;
    font-size: 15px;
    line-height: 17px;
  }

  /* Back */
  .back-art {
    position: absolute;
    inset: 0;
  }
  .back-url {
    position: absolute;
    left: 0;
    right: 0;
    top: 490px;
    margin: 0;
    text-align: center;
    font-size: 22px;
    line-height: 26px;
    font-weight: 700;
    letter-spacing: 1.8px;
    color: var(--card-white);
  }
</style>
</head>
<body>
<main class="canvas">

  <section class="card card--front" aria-label="Business card front">
    <div class="brand">
      <span class="brand__dot" aria-hidden="true"></span>
      <h1 class="brand__name">Tidewell Pest Solutions</h1>
    </div>

    <div class="contact">
      <p class="contact__name">LIAM CARTER</p>
      <p class="contact__role">Managing Director</p>
      <svg class="contact__icons" width="158" height="20" viewBox="0 0 158 20" aria-hidden="true">
        <line x1="0" y1="10" x2="42" y2="10" stroke="#777" stroke-width="1"/>
        <line x1="116" y1="10" x2="158" y2="10" stroke="#777" stroke-width="1"/>
        <circle cx="54" cy="10" r="9" fill="var(--charcoal)"/>
        <path d="M50.5 6.2 l1.8-0.6 1.2 2.3-1.1 0.9 c0.6 1.3 1.5 2.2 2.8 2.8 l0.9-1.1 2.3 1.2-0.6 1.8 c-3.6 0.3-7.6-3.7-7.3-7.3z" fill="#fff"/>
        <circle cx="79" cy="10" r="9" fill="var(--charcoal)"/>
        <rect x="74.5" y="6.8" width="9" height="6.4" fill="#fff"/>
        <path d="M74.5 6.8 l4.5 3.6 4.5-3.6" fill="none" stroke="var(--charcoal)" stroke-width="0.9"/>
        <circle cx="104" cy="10" r="9" fill="var(--charcoal)"/>
        <circle cx="104" cy="10" r="4.6" fill="none" stroke="#fff" stroke-width="1.2"/>
        <path d="M99.4 10 h9.2 M104 5.4 c-2.2 2.6-2.2 6.6 0 9.2 M104 5.4 c2.2 2.6 2.2 6.6 0 9.2" fill="none" stroke="#fff" stroke-width="0.9"/>
      </svg>
      <p class="contact__line">02-9184-3307</p>
      <p class="contact__line">hello@tidewellpest.com</p>
      <p class="contact__line">www.tidewellpest.com</p>
      <div class="contact__rule"></div>
      <p class="contact__address">48 Harbourline Road</p>
      <p class="contact__address">Sydney NSW, 2000</p>
    </div>
  </section>

  <section class="card card--back" aria-label="Business card back">
    <svg class="back-art" width="347" height="561" viewBox="0 0 347 561" aria-hidden="true">
      <path d="M0 227 C140 236 290 280 347 355 L347 561 L0 561 Z" fill="var(--brand-red)"/>
      <circle cx="186" cy="271" r="131" fill="var(--charcoal)" stroke="var(--card-white)" stroke-width="10"/>
    </svg>
    <p class="back-url">www.tidewellpest.com</p>
  </section>

</main>
</body>
</html>
```